Startup of Management Company looking for Designers!

I am looking for an upscale website. Veltrona will focus on Real Estate, Wealth Management, and Consulting,

Target Market(s)

investors, sellers of real estate, people looking to have their real estate management.
companies looking for consulting services

Number of Pages Required

5+ page

Font styles to use
Sans Serif

Requirements
Must have
• pictures, real.

```html
<!DOCTYPE html>
<html lang="en">
<head>
<meta charset="utf-8">
<title>Veltrona — Real Estate Management &amp; Consulting</title>
<link href="https://fonts.googleapis.com/css2?family=Rajdhani:wght@500;600;700&family=Raleway:wght@400;500;600&display=swap" rel="stylesheet">
<style>
:root{
  --navy:#0c2340;
  --ink:#1d1f24;
  --footer:#101a2a;
  --accent:#2a6fc9;
  --orange:#e8902a;
  --red:#e04848;
  --muted:#8a8f98;
  --light:#f4f4f5;
  --white:#ffffff;
}
*{margin:0;padding:0;box-sizing:border-box}
html,body{width:1200px;height:4508px;overflow:hidden;background:var(--white)}
body{position:relative;font-family:'Raleway',sans-serif;color:var(--ink)}
.abs{position:absolute}
.h{font-family:'Rajdhani',sans-serif;font-weight:700;text-transform:uppercase;letter-spacing:.5px}
.btn{position:absolute;display:flex;align-items:center;justify-content:center;font-family:'Raleway',sans-serif;font-size:15px;font-weight:500;letter-spacing:.5px;text-transform:uppercase}
.btn.dark{background:var(--ink);color:var(--white)}
.btn.light{background:var(--white);color:var(--ink)}
.para{font-size:16px;line-height:29px;color:var(--muted)}

/* hero */
.hero{left:0;top:0;width:1200px;height:873px;background:linear-gradient(120deg,#6b6f74 0%,#3f434a 45%,#2a2e35 100%)}
.hero-shade{left:0;top:0;width:1200px;height:873px;background:linear-gradient(90deg,rgba(20,22,26,.55),rgba(20,22,26,.15))}
.topmail{left:65px;top:10px;color:#ddd;font-size:14px;display:flex;align-items:center;gap:7px}
.social-top{top:10px;display:flex;gap:16px;right:65px}
.social-top span{width:18px;height:18px;border:2px solid #fff;border-radius:50%}
.logo{left:65px;top:58px;color:#fff;font-family:'Rajdhani',sans-serif;font-weight:700;font-size:26px;letter-spacing:1px}
.nav{top:64px;right:63px;display:flex;gap:52px;color:#fff;font-size:13px;text-transform:uppercase}
.nav .on{font-weight:600}
.eyebrow{left:66px;top:194px;color:var(--orange);font-size:17px;text-transform:uppercase;display:flex;align-items:center;gap:10px}
.eyebrow i{display:block;width:100px;height:1px;background:#fff}
.hero-title{left:65px;top:222px;color:#fff;font-size:46px;line-height:48px}
.hero-sub{left:66px;top:336px;color:#eee;font-size:16px;line-height:26px;width:460px}
.scroll{left:1156px;top:280px;color:#fff;font-size:12px;letter-spacing:3px;writing-mode:vertical-rl;text-transform:uppercase}
.scroll-line{left:1166px;top:410px;width:1px;height:170px;background:rgba(255,255,255,.6)}
.feat{top:595px;width:257px;height:229px;background:rgba(18,20,24,.72);color:#fff;padding:21px 12px}
.feat .ico{width:52px;height:52px}
.feat h3{font-family:'Rajdhani',sans-serif;font-weight:600;font-size:22px;line-height:28px;margin-top:24px;text-transform:uppercase}
.feat p{font-size:14px;line-height:22px;color:#ccc;margin-top:8px}

/* welcome */
.navyblock{left:0;top:873px;width:373px;height:511px;background:var(--navy)}
.welcome-img{left:65px;top:971px;width:414px;height:385px;background:linear-gradient(135deg,#b9c0c8,#3c434d 55%,#1b1f26)}
.welcome-eye{left:528px;top:998px;font-size:14px;color:#555;display:flex;align-items:center;gap:12px;text-transform:uppercase}
.welcome-eye i{display:block;width:180px;height:1px;background:var(--red)}
.welcome-title{left:526px;top:1030px;font-size:40px;line-height:44px;color:var(--ink)}
.welcome-text{left:528px;top:1137px;width:610px}

/* focus */
.sec-title{left:0;width:1200px;text-align:center;font-size:40px;color:var(--ink)}
.sec-sub{left:0;width:1200px;text-align:center;font-size:14px;color:#666}
.focus-title{font-family:'Rajdhani',sans-serif;font-weight:600;font-size:29px;color:var(--ink)}
.focus-title b{color:var(--accent);font-weight:600}
.focus-img{height:327px;width:483px}
.f1{left:0;top:1595px;clip-path:polygon(0 0,315px 0,483px 290px,483px 300px,460px 327px,0 327px);background:linear-gradient(180deg,#8cb5dc 0%,#bfd6e9 30%,#3d6e2b 55%,#5f9a35 100%)}
.f2{left:717px;top:2022px;clip-path:polygon(228px 0,483px 0,483px 327px,25px 327px,0 300px,0 290px);background:linear-gradient(135deg,#cfd6dd,#f1f1f1 45%,#c79b6b 75%,#a67648)}
.f3{left:0;top:2449px;clip-path:polygon(0 0,315px 0,483px 290px,483px 300px,460px 327px,0 327px);background:linear-gradient(135deg,#3b4452,#6d6a66 45%,#2a3040)}

/* trusted */
.trusted{left:0;top:2875px;width:1200px;height:277px;background:var(--light)}
.badge{width:175px;height:75px;background:#fff;box-shadow:0 1px 4px rgba(0,0,0,.08);display:flex;align-items:center;justify-content:center}
.badge span{width:90px;height:28px;background:#d6dbe2;border-radius:4px}

/* blog */
.blog-img{top:3306px;width:350px;height:224px}
.blog-t{top:3555px;width:330px;font-size:20px;line-height:29px;font-weight:500;color:var(--ink)}
.blog-p{top:3624px;width:340px;font-size:14px;line-height:24px;color:var(--muted)}

/* contact band */
.band{left:0;top:3860px;width:1200px;height:317px;background:linear-gradient(120deg,#2a3a58,#1b2a46 50%,#22324f)}
.band-title{color:#fff}
.band-text{left:170px;top:4020px;width:860px;text-align:center;color:#e6e9ef;font-size:16px;line-height:27px}

/* footer */
.footer{left:0;top:4177px;width:1200px;height:331px;background:var(--footer)}
.fcol{top:4218px;color:#c3c8d0;font-size:13px}
.fcol h4{font-family:'Rajdhani',sans-serif;font-weight:600;color:#fff;font-size:20px;text-transform:uppercase;letter-spacing:.5px;margin-bottom:14px}
.fcol li{list-style:none;height:35px}
.fcontact li{display:flex;gap:10px;height:auto;margin-bottom:22px;line-height:18px}
.fsocial li{display:flex;align-items:center;gap:10px;height:38px}
.fsocial li span{width:26px;height:26px;border-radius:50%;background:#fff}
.copy{left:0;top:4445px;width:1200px;text-align:center;font-size:12px;color:#8a93a2}
.copy b{color:#fff;font-weight:600}
</style>
</head>
<body>

<!-- HERO -->
<div class="abs hero" role="img" aria-label="Photo of business people in a meeting, a man in a suit seated holding papers"></div>
<div class="abs hero-shade"></div>
<div class="abs topmail">
  <svg width="14" height="10" viewBox="0 0 14 10"><rect x="0.5" y="0.5" width="13" height="9" fill="none" stroke="#ddd"/><path d="M0.5 0.5 7 6 13.5 0.5" fill="none" stroke="#ddd"/></svg>
  info@veltronagroup.com
</div>
<div class="abs social-top" aria-label="Social links"><span></span><span></span><span></span></div>
<div class="abs logo">VELTRONA</div>
<nav class="abs nav"><span class="on">Home</span><span>About Us</span><span>Services</span><span>Blog</span><span>Contact Us</span></nav>

<div class="abs eyebrow">Duis Irure <i></i></div>
<h1 class="abs h hero-title">Ratione Voluptatem<br>Sequi Nesciunt</h1>
<p class="abs hero-sub">But I must explain to you how all this mistaken idea of denouncing pleasure and praising pain</p>
<div class="btn light" style="left:66px;top:399px;width:151px;height:52px">Get Started</div>
<div class="abs scroll">Scroll Down</div>
<div class="abs scroll-line"></div>

<div class="abs feat" style="left:65px">
  <svg class="ico" viewBox="0 0 52 52" fill="none" stroke="#fff" stroke-width="2"><rect x="6" y="4" width="24" height="32"/><path d="M11 12h14M11 18h14M11 24h10"/><circle cx="38" cy="38" r="9"/></svg>
  <h3>Excepteur Sint<br>Occaecat Cupidatat</h3>
  <p>Sed ut perspiciatis unde omnis iste natus error sit voluptatem</p>
</div>
<div class="abs feat" style="left:336px">
  <svg class="ico" viewBox="0 0 52 52" fill="none" stroke="#fff" stroke-width="2"><rect x="4" y="6" width="44" height="30"/><path d="M20 36v8M32 36v8M14 44h24M10 14h20M10 20h14"/></svg>
  <h3>Excepteur Sint<br>Occaecat Cupidatat</h3>
  <p>Sed ut perspiciatis unde omnis iste natus error sit voluptatem</p>
</div>
<div class="abs feat" style="left:607px">
  <svg class="ico" viewBox="0 0 52 52" fill="none" stroke="#fff" stroke-width="2"><rect x="8" y="24" width="36" height="4"/><path d="M12 28v18M40 28v18"/><circle cx="26" cy="12" r="5"/><circle cx="12" cy="18" r="3"/><circle cx="40" cy="18" r="3"/></svg>
  <h3>Excepteur Sint<br>Occaecat Cupidatat</h3>
  <p>Sed ut perspiciatis unde omnis iste natus error sit voluptatem</p>
</div>
<div class="abs feat" style="left:876px">
  <svg class="ico" viewBox="0 0 52 52" fill="none" stroke="#fff" stroke-width="2"><rect x="4" y="20" width="20" height="26"/><path d="M8 26h12M8 32h4M16 32h4M8 38h4M16 38h4"/><circle cx="34" cy="18" r="12"/><path d="M34 11v14M30 14h6a3 3 0 0 1 0 6h-4a3 3 0 0 0 0 6h6"/></svg>
  <h3>Excepteur Sint<br>Occaecat Cupidatat</h3>
  <p>Sed ut perspiciatis unde omnis iste natus error sit voluptatem</p>
</div>

<!-- WELCOME -->
<div class="abs navyblock"></div>
<div class="abs welcome-img" role="img" aria-label="Photo of a businessman in a suit holding a miniature glowing city skyline in his palm"></div>
<div class="abs welcome-eye">Welcome to <i></i></div>
<h2 class="abs h welcome-title">Real Estate<br>Management &amp; Consulting</h2>
<p class="abs para welcome-text">Sed ut perspiciatis unde omnis iste natus error sit voluptatem accusantium doloremque laudantium, totam rem aperiam, eaque ipsa quae ab illo inventore veritatis et quasi architecto beatae vitae dicta sunt explicabo. Nemo enim ipsam voluptatem quia voluptas...</p>
<div class="btn dark" style="left:528px;top:1274px;width:144px;height:52px">Read More</div>

<!-- FOCUS -->
<h2 class="abs h sec-title" style="top:1472px">Our Focus</h2>
<p class="abs sec-sub" style="top:1521px">Duis aute irure dolor in reprehenderit in voluptate velit esse cillum</p>

<div class="abs focus-img f1" role="img" aria-label="Photo of a large country house behind green lawns and trees"></div>
<h3 class="abs focus-title" style="left:523px;top:1636px">Real <b>Estate</b></h3>
<p class="abs para" style="left:523px;top:1683px;width:610px">Sed ut perspiciatis unde omnis iste natus error sit voluptatem accusantium doloremque laudantium, totam rem aperiam, eaque ipsa quae ab illo inventore veritatis et quasi architecto beatae vitae dicta sunt explicabo. Nemo enim ipsam voluptatem quia voluptas...</p>
<div class="btn dark" style="left:523px;top:1822px;width:144px;height:53px">Read More</div>

<h3 class="abs focus-title" style="left:65px;top:2061px">Wealth <b>Management</b></h3>
<p class="abs para" style="left:65px;top:2109px;width:610px">Sed ut perspiciatis unde omnis iste natus error sit voluptatem accusantium doloremque laudantium, totam rem aperiam, eaque ipsa quae ab illo inventore veritatis et quasi architecto beatae vitae dicta sunt explicabo. Nemo enim ipsam voluptatem quia voluptas...</p>
<div class="btn dark" style="left:65px;top:2250px;width:144px;height:53px">Read More</div>
<div class="abs focus-img f2" role="img" aria-label="Photo of hands stacking wooden blocks in a tower game"></div>

<div class="abs focus-img f3" role="img" aria-label="Photo of a business team meeting around a table"></div>
<h3 class="abs focus-title" style="left:523px;top:2488px">Consulting</h3>
<p class="abs para" style="left:523px;top:2536px;width:610px">Sed ut perspiciatis unde omnis iste natus error sit voluptatem accusantium doloremque laudantium, totam rem aperiam, eaque ipsa quae ab illo inventore veritatis et quasi architecto beatae vitae dicta sunt explicabo. Nemo enim ipsam voluptatem quia voluptas...</p>
<div class="btn dark" style="left:523px;top:2676px;width:144px;height:53px">Read More</div>

<!-- TRUSTED -->
<div class="abs trusted"></div>
<div class="abs badge" style="left:65px;top:2930px" aria-label="Partner badge"><span></span></div>
<div class="abs badge" style="left:257px;top:2930px" aria-label="Partner badge"><span></span></div>
<div class="abs badge" style="left:65px;top:3022px" aria-label="Partner badge"><span></span></div>
<div class="abs badge" style="left:257px;top:3022px" aria-label="Partner badge"><span></span></div>
<p class="abs" style="left:491px;top:2950px;font-size:14px;color:#444;text-transform:uppercase">We Are</p>
<h2 class="abs h" style="left:491px;top:2966px;font-size:40px;color:var(--ink)">Trusted</h2>
<p class="abs para" style="left:491px;top:3022px;width:640px">Sed ut perspiciatis unde omnis iste natus error sit voluptatem accusantium doloremque laudantium, totam rem aperiam</p>

<!-- BLOG -->
<h2 class="abs h sec-title" style="top:3240px">Recent Blog</h2>

<div class="abs blog-img" style="left:65px;background:linear-gradient(135deg,#c9b79d,#f0ede8 45%,#8f99a4)" role="img" aria-label="Photo of a hand reaching toward small white model houses"></div>
<h3 class="abs blog-t" style="left:65px">Neque porro quisquam est qui dolorem</h3>
<p class="abs blog-p" style="left:65px">Sed ut perspiciatis unde omnis iste natus error sit voluptatem accusantium doloremque laudantium</p>
<div class="btn dark" style="left:65px;top:3708px;width:144px;height:52px">Read More</div>

<div class="abs blog-img" style="left:425px;background:linear-gradient(135deg,#dfe3e6,#f4f5f6 40%,#3b3f46 70%,#b8bcc2)" role="img" aria-label="Photo of business people walking through a bright office"></div>
<h3 class="abs blog-t" style="left:425px">Neque porro quisquam est qui dolorem</h3>
<p class="abs blog-p" style="left:425px">Sed ut perspiciatis unde omnis iste natus error sit voluptatem accusantium doloremque laudantium</p>
<div class="btn dark" style="left:425px;top:3708px;width:144px;height:52px">Read More</div>

<div class="abs blog-img" style="left:785px;background:linear-gradient(135deg,#3a5a8a,#7d8a95 40%,#c9d23a 65%,#4a4e55)" role="img" aria-label="Photo of construction workers in hard hats reviewing plans"></div>
<h3 class="abs blog-t" style="left:785px">Neque porro quisquam est qui dolorem</h3>
<p class="abs blog-p" style="left:785px">Sed ut perspiciatis unde omnis iste natus error sit voluptatem accusantium doloremque laudantium</p>
<div class="btn dark" style="left:785px;top:3708px;width:144px;height:52px">Read More</div>

<!-- CONTACT BAND -->
<div class="abs band" role="img" aria-label="Photo of a hand writing on documents at a desk, tinted dark blue"></div>
<h2 class="abs h sec-title band-title" style="top:3955px">Contact Us Today!</h2>
<p class="abs band-text">Sed ut perspiciatis unde omnis iste natus error sit voluptatem accusantium doloremque laudantium, totam rem aperiam, eaque ipsa quae ab illo inventore veritatis...</p>

<!-- FOOTER -->
<div class="abs footer"></div>
<div class="abs fcol" style="left:65px"><h4>Quick Links</h4><ul><li>Home</li><li>About Us</li><li>Services</li><li>Blog</li><li>Contact Us</li></ul></div>
<div class="abs fcol" style="left:245px"><h4>Focus</h4><ul><li>Real Estate</li><li>Wealth Management</li><li>Consulting</li></ul></div>
<div class="abs fcol" style="left:443px"><h4>Services</h4><ul><li>Finibus Bonorum Malorum</li><li>Finibus Bonorum</li><li>Finibus Bonorum Malorum</li><li>Finibus Bonorum</li></ul></div>
<div class="abs fcol fcontact" style="left:694px"><h4>Contact Us</h4><ul>
  <li><svg width="12" height="16" viewBox="0 0 12 16"><path d="M6 0a6 6 0 0 1 6 6c0 4-6 10-6 10S0 10 0 6a6 6 0 0 1 6-6z" fill="#fff"/><circle cx="6" cy="6" r="2" fill="#101a2a"/></svg><span>42 Harbor Row, Northfield<br>2500 USA</span></li>
  <li><svg width="14" height="14" viewBox="0 0 14 14"><path d="M3 0l3 3-2 2a8 8 0 0 0 5 5l2-2 3 3-2 3C6 14 0 8 0 3z" fill="#fff"/></svg><span>+1(555) 240 7719</span></li>
  <li><svg width="14" height="10" viewBox="0 0 14 10"><rect x="0.5" y="0.5" width="13" height="9" fill="none" stroke="#fff"/><path d="M0.5 0.5 7 6 13.5 0.5" fill="none" stroke="#fff"/></svg><span>info@veltronagroup.com</span></li>
</ul></div>
<div class="abs fcol fsocial" style="left:1009px"><h4>Follow Us</h4><ul><li><span></span>Newsroom</li><li><span></span>Updates</li><li><span></span>Gallery</li></ul></div>
<p class="abs copy">COPYRIGHT © 2021 <b>VELTRONA</b> ALL RIGHTS RESERVED.</p>

</body>
</html>
```